NYC and MIAMI Trendy Womans Boutique Custom Mailing Packaging

Im looking for help designing custom mailing pouches for my woman's retail store. Weve been doing a lot of online sales lately and Its time to upgrade to custom packaging. I want it to look fun and playful but not too childish or cheesy.
Please see our website www.lorvashop.com and our instagram account @lorvashop to get a feel for our brand.

Target Market(s)

From teens- 60 year old

Industry/Entity Type

Clothing Brand

Colors
feeeee
fff9f9
fdf3f8

Requirements
Must have
• Pink :) I need it to be girly, fun, but also classy and sophisticated
Should not have
• Look childish or cheesy

```html
<!DOCTYPE html>
<html lang="en">
<head>
<meta charset="UTF-8">
<title>Lorva – Mailer Pouch</title>
<link href="https://fonts.googleapis.com/css2?family=Playfair+Display:wght@500&display=swap" rel="stylesheet">
<style>
  :root {
    --backdrop: #e6e4e6;
    --pouch-black: #0c0a0b;
    --pouch-dot: #2a2729;
    --blush: #e3a3c0;
    --blush-light: #efbcd6;
    --white: #f7f3f5;
  }
  html, body {
    margin: 0;
    padding: 0;
    width: 1200px;
    height: 900px;
    overflow: hidden;
    background: var(--backdrop);
  }
  .canvas {
    position: relative;
    width: 1200px;
    height: 900px;
  }
  .mailer {
    position: absolute;
    left: 0;
    top: 0;
  }
  .brand-name {
    font-family: "Playfair Display", serif;
    font-weight: 500;
    font-size: 44px;
    letter-spacing: 4px;
    fill: var(--white);
  }
</style>
</head>
<body>
<main class="canvas">
  <svg class="mailer" width="1200" height="900" viewBox="0 0 1200 900" xmlns="http://www.w3.org/2000/svg">
    <defs>
      <radialGradient id="pouch-surface" cx="50%" cy="45%" r="70%">
        <stop offset="0%" stop-color="#1c191b"/>
        <stop offset="100%" stop-color="#0c0a0b"/>
      </radialGradient>
      <linearGradient id="band-fill" x1="0" y1="0" x2="0" y2="1">
        <stop offset="0%" stop-color="#efbcd6"/>
        <stop offset="100%" stop-color="#e3a3c0"/>
      </linearGradient>
    </defs>

    <rect class="pouch-body" x="336" y="138" width="529" height="638"
          fill="url(#pouch-surface)" role="img"
          aria-label="Black surface with a grid of soft grey polka dots"/>

    <g class="seal-band">
      <rect x="492" y="138" width="218" height="306" fill="url(#band-fill)"/>
      <circle cx="601" cy="444" r="106" fill="#e3a3c0" stroke="#f7f3f5" stroke-width="2"/>
    </g>

    <text class="brand-name" x="601" y="459" text-anchor="middle">LORVA</text>
  </svg>
</main>
</body>
</html>
```